Hospital Website Design - PSD only

We need a web design for a community hospital based in Uniontown, Pennsylvania.

We would like to see a first round of designs for the website HOMEPAGE. Once we have selected finalists for the look & feel, based on the submitted homepage designs, we will request an additional INTERNAL page design.

Both designs should follow the content requirements displayed on the attached wireframes. I will post the internal page wireframe after the homepage design finalists are selected.

The desired Look & Feel for the website is clean and modern.

3 sites we like are:
http://www.marvellcare.org/
http://www.qrtm.org/
http://www.dellwyn.org/

Attached are the Homepage wireframe, and the Brackfield Hospital Logo.

The winning design will communicate a bright, healthy, energetic, community-oriented feeling.

Please note that readability is very important for a hospital website. Font-sizes and line-heights should be carefully selected for comfortable reading.
Updates

Dear designers -- Please don't feel locked into the exact shades of blue / brown used in the logo. We find this color scheme quite ugly and are working on a logo update. The new color scheme will probably still involve some shades of blue and brown, but we aren't sure yet. Please use your best judgement to make a beautiful design, similar in style to the modern / simple aesthetic of http://www.marvellcare.org/ We will be working on feedback to designs today. Thank you.

Regarding Large Rotating Graphic area and Navigation: We prefer a full-width display, rather than boxed. The navigation should be visually prominent, easy to read text that one can scan easily across the top of the page. Again, please refer to http://www.marvellcare.org/ for our preferred design aesthetic. Some of the designs submitted have been somewhat dated in their styling. We'd like a polished, modern, crisp, bold, beautiful design.

Re: choice of image in large rotating graphic area -- Designers, please do not use stock photography of a group of doctors, or a nursing home scene, in your sample rotating graphic areas. Although this should not affect our perception of the design, it throws off everything in the page if we don't like the image. Please try to select a bold / attractive image that you would like to set the tone for your design.

Reason: Extending our deadline to receive more designs exploring other color options containing less brown, or browns with a more attractive vibe. We would also like to see designs that are not exact replicas of the wireframe. The wireframe is just to show the elements on the page. Please use your creativity to utilize these elements in an attractive layout that we will like. We would also prefer to see use of photography that shows a younger, more cheerful, hopeful feeling in the design... and where the photographs are consistent with your design approach. Thanks!

In general, feedback for everyone is, please look here: http://www.marvellcare.org/ that's the feeling / vibe we want. DO NOT let the old, ugly, outdated logo determine your design. We are having the logo redesigned. DO NOT take an ugly, outdated template, and adapt it for this website. We want to see something BEAUTIFUL!!! Please give us your best effort! People who come to this website are in health crisis, and they want to be uplifted!! Their good spirits are in your hands.

Reason: We are still reviewing submissions and working with designers to provide better feedback. Thanks for your patience.

Reason: our sincerest apologies for the failure to provide adequate feedback this week. We hit a snag with the various decision makers on this project and were not able to review the recent submissions. We will make every effort to have a decision by tomorrow. Thank you for your patience.

Target Market(s)

Adults based in suburban & rural community, aged 18-80.

Industry/Entity Type

Hospital

Requirements
Must have
• The design must include all of the content areas outlined on the attached wireframe.
The design must include the attached logo. (Note, we may update the logo during the design contest, but it will not be changed dramatically. It will just be modernized slightly.)
Nice to have
• Show hover states for things like Navigation, Links, or small images in gallery, so we can see how you imagine interactive states.

```html
<!DOCTYPE html>
<html lang="en">
<head>
<meta charset="utf-8">
<title>Brackfield Hospital</title>
<link href="https://fonts.googleapis.com/css2?family=Open+Sans:wght@400;600;700&display=swap" rel="stylesheet">
<style>
:root{
  --brown:#6b4423;
  --brown-dark:#4a2d15;
  --blue:#1d68b0;
  --blue-mid:#2c7cc4;
  --blue-light:#4d97d6;
  --blue-pale:#cfe3f3;
  --page:#e9eaec;
  --panel:#ffffff;
  --text:#555a60;
  --ink:#2f3338;
  --muted:#8a8f95;
  --line:#d7d9dc;
}
*{box-sizing:border-box;margin:0;padding:0}
html,body{width:1200px;height:2708px;overflow:hidden}
body{font-family:"Open Sans",Arial,sans-serif;color:var(--text);background:var(--page);position:relative;font-size:15px;line-height:1.55}
a{color:inherit;text-decoration:none}
.wrap{width:1000px;margin:0 auto;position:relative}

/* top bar */
.topbar{height:40px;background:var(--brown-dark);color:#f1e6da;font-size:13px}
.topbar .wrap{display:flex;align-items:center;height:40px;justify-content:space-between}
.topbar .contact{display:flex;gap:26px;align-items:center}
.topbar .contact span{display:flex;align-items:center;gap:7px}
.topbar .utility{display:flex;gap:22px;align-items:center}
.lang{border:1px solid #a88a6c;padding:0 8px;font-size:12px}

/* header */
.header{height:132px;background:#fff}
.header .wrap{display:flex;justify-content:space-between;align-items:center;height:132px}
.brand{display:flex;align-items:center;gap:12px}
.brand-mark{width:18px;height:18px;border-radius:50%;background:var(--brown)}
.brand-name{font-size:30px;font-weight:600;color:var(--ink);line-height:1}
.brand-tag{font-size:12px;color:var(--muted);margin-top:8px}
.search{display:flex;width:250px;height:36px;border:1px solid var(--brown)}
.search span{flex:1;padding:0 12px;line-height:34px;font-size:13px;color:var(--muted)}
.search b{width:40px;background:var(--brown);display:flex;align-items:center;justify-content:center}

/* nav */
.nav{height:60px;background:#f6f6f6;border-top:1px solid var(--line);border-bottom:1px solid var(--line)}
.nav ul{list-style:none;display:flex;height:58px;align-items:stretch}
.nav li{display:flex;align-items:center;padding:0 21px;font-size:15px;font-weight:600;color:#3a3f45;border-right:1px solid var(--line);white-space:nowrap}
.nav li.active{background:var(--blue);color:#fff}

/* hero */
.hero{height:540px;position:relative;background:linear-gradient(90deg,#1a5fa5 0%,#3d86c8 35%,#b9d3ea 60%,#e9f0f6 100%)}
.hero-photo{position:absolute;right:0;top:0;width:560px;height:540px;background:radial-gradient(ellipse at 55% 45%,#f4f6f8 0%,#dfe7ee 55%,rgba(223,231,238,0) 85%)}
.hero h1{position:absolute;left:100px;top:150px;width:540px;color:#fff;font-size:42px;font-weight:600;line-height:1.25}
.dots{height:60px;background:#fff;display:flex;justify-content:center;align-items:center;gap:12px}
.dots i{width:12px;height:12px;border-radius:50%;background:var(--blue-pale)}
.dots i.on{background:var(--blue)}

/* steps */
.steps{height:130px;background:#fff;padding-top:30px}
.steps svg{display:block}

/* content */
.content{padding-top:30px}
.panel{background:var(--panel);box-shadow:0 1px 3px rgba(0,0,0,.08)}
.btn{display:inline-block;background:var(--blue);color:#fff;font-size:13px;font-weight:600;padding:6px 20px}
h2.section{color:var(--blue);font-size:22px;font-weight:700;text-transform:uppercase;letter-spacing:.5px;margin-bottom:12px}

.intro{height:300px;display:flex;padding:28px 30px}
.about{width:300px;padding-right:30px;border-right:1px solid var(--line);font-size:13.5px;line-height:1.6}
.about p{margin-bottom:12px}
.about .btn{float:right}
.videos{flex:1;padding-left:30px;position:relative}
.video-main{position:absolute;left:30px;top:42px;width:260px}
.player{height:140px;background:#1e1f22;position:relative}
.player .bar{position:absolute;left:0;right:0;bottom:0;height:18px;background:#333}
.player .prog{position:absolute;left:8px;bottom:7px;width:90px;height:4px;background:var(--blue-light)}
.video-main h3{font-size:15px;font-weight:600;color:#333;margin-top:8px}
.video-meta{display:flex;justify-content:space-between;font-size:11px;color:var(--muted)}
.video-meta b{color:#333}
.video-list{position:absolute;left:320px;top:42px;width:280px;list-style:none}
.video-list li{display:flex;gap:10px;margin-bottom:12px;font-size:12px;line-height:1.35}
.thumb{width:90px;height:52px;flex:none;background:linear-gradient(135deg,#f2f2f2,#d3d6da)}
.video-list strong{display:block;color:#333;font-weight:600}
.video-list small{color:var(--muted);font-size:11px}
.videos .btn{position:absolute;right:0;bottom:0}

.resources{height:300px;margin-top:30px;display:flex;align-items:flex-start}
.doctor-photo{width:150px;height:280px;background:linear-gradient(180deg,#f0f3f6 0%,#d6dde4 100%);margin-right:20px}
.res-list{width:420px;padding-top:10px}
.res-list ul{list-style:none}
.res-list li{display:flex;align-items:center;gap:12px;font-size:15px;color:#333;padding:10px 0;border-bottom:1px solid var(--line)}
.res-list li:last-child{border-bottom:0}
.access{margin-left:auto;width:390px;display:flex;flex-direction:column;gap:22px}
.access-box{height:130px;background:var(--blue-mid);display:flex;flex-direction:column;color:#fff}
.access-box .top{flex:1;display:flex;align-items:center;gap:26px;padding:0 30px}
.access-box .top span{font-size:30px;font-weight:600}
.access-box .cta{height:36px;background:var(--blue);text-align:right;padding:0 24px;line-height:36px;font-weight:600;font-size:15px}

.news{height:590px;margin-top:20px;padding:26px 30px}
.tabs{display:flex;border-bottom:3px solid var(--blue);margin-bottom:30px}
.tabs span{padding:8px 24px;font-size:18px;font-weight:700;color:var(--blue)}
.tabs span.active{background:var(--blue);color:#fff}
.cards{display:flex;gap:40px}
.card{width:280px;font-size:14px;line-height:1.55}
.card .photo{height:210px;margin-bottom:18px}
.card p{margin-bottom:14px}
.card .btn{float:right}
.p1{background:linear-gradient(135deg,#e8eef3,#b6c8d8)}
.p2{background:linear-gradient(135deg,#f3f5f7,#aec6dc)}
.p3{background:linear-gradient(135deg,#e3edf4,#8fb3d3)}

/* footer */
.footer{position:absolute;left:0;top:2380px;width:1200px;height:328px;background:var(--brown);color:#f1e6da}
.footer .cols{display:flex;padding-top:26px;height:240px}
.footer h4{font-size:17px;font-weight:700;color:#fff;margin-bottom:10px}
.f-address{width:400px;display:flex;flex-wrap:wrap;align-content:flex-start}
.f-address h4{width:100%}
.map{width:150px;height:140px;background:linear-gradient(135deg,#e9e3d6,#c9d7e3);margin-right:16px}
.f-address p{width:220px;font-size:12px;line-height:1.55}
.f-links{width:310px;padding-left:20px}
.f-links ul{list-style:none;font-size:12.5px;line-height:1.75}
.f-about{flex:1;padding-left:20px}
.f-about .row{display:flex;align-items:center;gap:14px;font-size:15px;margin-bottom:14px}
.f-about .row.h{font-size:17px;font-weight:700;color:#fff}
.ico{width:30px;height:30px;display:flex;align-items:center;justify-content:center;flex:none}
.footbar{position:absolute;left:0;bottom:0;width:1200px;height:88px;background:var(--brown-dark)}
.footbar .wrap{display:flex;justify-content:space-between;align-items:center;height:88px}
.footbar .links{font-size:12.5px;line-height:1.7}
.footbar .links div:first-child{font-size:11.5px;color:#c7b39e}
.social{display:flex;gap:10px}
.social i{width:28px;height:28px;background:#86613d;display:block}
</style>
</head>
<body>

<div class="topbar">
  <div class="wrap">
    <div class="contact">
      <span><svg width="13" height="13" viewBox="0 0 24 24"><path fill="#f1e6da" d="M6.6 10.8a15 15 0 006.6 6.6l2.2-2.2c.3-.3.7-.4 1-.2 1.1.4 2.3.6 3.6.6.6 0 1 .4 1 1V20c0 .6-.4 1-1 1C10.6 21 3 13.4 3 4c0-.6.4-1 1-1h3.5c.6 0 1 .4 1 1 0 1.3.2 2.5.6 3.6.1.3 0 .7-.2 1z"/></svg>(555) 210-4400</span>
      <span><svg width="14" height="11" viewBox="0 0 24 18"><rect x="1" y="1" width="22" height="16" fill="none" stroke="#f1e6da" stroke-width="2"/><path d="M1 1l11 9 11-9" fill="none" stroke="#f1e6da" stroke-width="2"/></svg>brackfield-hospital@info.com</span>
    </div>
    <div class="utility"><a>Home</a><a>Sitemap</a><a>Giving</a><span class="lang">EN ▾</span></div>
  </div>
</div>

<header class="header">
  <div class="wrap">
    <div class="brand">
      <div class="brand-mark"></div>
      <div>
        <div class="brand-name">Brackfield Hospital</div>
        <div class="brand-tag">Caring for our neighbours every day of the year</div>
      </div>
    </div>
    <div class="search"><span>Search</span><b><svg width="16" height="16" viewBox="0 0 24 24"><circle cx="10" cy="10" r="7" fill="none" stroke="#fff" stroke-width="2.5"/><path d="M15 15l6 6" stroke="#fff" stroke-width="2.5"/></svg></b></div>
  </div>
</header>

<nav class="nav">
  <div class="wrap">
    <ul>
      <li class="active">Home</li>
      <li>Our services</li>
      <li>Facilities &amp; Directions</li>
      <li>Patient &amp; Visitor information</li>
      <li>Find a doctor</li>
      <li>Health &amp; Wellness</li>
    </ul>
  </div>
</nav>

<section class="hero">
  <div class="hero-photo" role="img" aria-label="Smiling young doctor with a stethoscope around his neck"></div>
  <h1>Good health and good sense are two of life's greatest blessings</h1>
</section>
<div class="dots"><i></i><i class="on"></i><i></i><i></i><i></i></div>

<section class="steps">
  <div class="wrap">
    <svg width="1000" height="80" viewBox="0 0 1000 80" font-family="Open Sans, Arial, sans-serif" font-size="18" font-weight="600">
      <polygon points="0,0 240,0 270,40 240,80 0,80" fill="#6b4423"/>
      <polygon points="250,0 490,0 520,40 490,80 250,80 280,40" fill="#1d68b0"/>
      <polygon points="500,0 740,0 770,40 740,80 500,80 530,40" fill="#2c7cc4"/>
      <polygon points="750,0 1000,0 1000,80 750,80 780,40" fill="#4d97d6"/>
      <text x="125" y="46" fill="#fff" text-anchor="middle">Symptom Checker</text>
      <text x="385" y="46" fill="#fff" text-anchor="middle">Schedule a Lab Test</text>
      <text x="635" y="46" fill="#fff" text-anchor="middle">Online Bill Pay</text>
      <text x="890" y="46" fill="#fff" text-anchor="middle">Support Our Work</text>
    </svg>
  </div>
</section>

<main class="content">
  <div class="wrap">
    <section class="panel intro">
      <div class="about">
        <h2 class="section">About Us</h2>
        <p>Lorem Ipsum is simply dummy text of the printing and typesetting industry. Lorem Ipsum has been the industry's standard dummy text ever since the 1500s, when an unknown printer took a galley of type and scrambled it to make a type specimen book.</p>
        <a class="btn">Read More</a>
      </div>
      <div class="videos">
        <h2 class="section">Videos</h2>
        <div class="video-main">
          <div class="player"><div class="bar"></div><div class="prog"></div>
            <svg style="position:absolute;left:115px;top:45px" width="30" height="34" viewBox="0 0 30 34"><polygon points="0,0 30,17 0,34" fill="#fff"/></svg></div>
          <h3>Lorem Ipsum is simply dummy</h3>
          <div class="video-meta"><span>By Brackfield Hospital</span><b>17,086</b></div>
        </div>
        <ul class="video-list">
          <li><div class="thumb" role="img" aria-label="Video still of a red heart model"></div><div><strong>Lorem Ipsum is simply dummy</strong><small>By Brackfield Hospital</small></div></li>
          <li><div class="thumb" role="img" aria-label="Video still of a red heart model"></div><div><strong>Lorem Ipsum is simply dummy</strong><small>By Brackfield Hospital</small></div></li>
          <li><div class="thumb" role="img" aria-label="Video still of a red heart model"></div><div><strong>Lorem Ipsum is simply dummy</strong><small>By Brackfield Hospital</small></div></li>
        </ul>
        <a class="btn">More Videos</a>
      </div>
    </section>

    <section class="resources">
      <div class="doctor-photo" role="img" aria-label="Senior doctor in a white coat with arms crossed"></div>
      <div class="res-list">
        <h2 class="section">Patient Resources</h2>
        <ul>
          <li><svg width="8" height="12" viewBox="0 0 8 12"><path d="M1 1l5 5-5 5" fill="none" stroke="#1d68b0" stroke-width="2"/></svg>Tips on Choosing the Right Doctor</li>
          <li><svg width="8" height="12" viewBox="0 0 8 12"><path d="M1 1l5 5-5 5" fill="none" stroke="#1d68b0" stroke-width="2"/></svg>Billing, Forms, &amp; Medical</li>
          <li><svg width="8" height="12" viewBox="0 0 8 12"><path d="M1 1l5 5-5 5" fill="none" stroke="#1d68b0" stroke-width="2"/></svg>Records</li>
          <li><svg width="8" height="12" viewBox="0 0 8 12"><path d="M1 1l5 5-5 5" fill="none" stroke="#1d68b0" stroke-width="2"/></svg>Making the Most of Your</li>
          <li><svg width="8" height="12" viewBox="0 0 8 12"><path d="M1 1l5 5-5 5" fill="none" stroke="#1d68b0" stroke-width="2"/></svg>Appointment</li>
        </ul>
      </div>
      <div class="access">
        <div class="access-box">
          <div class="top"><svg width="50" height="60" viewBox="0 0 50 60"><path d="M12 26V16a13 13 0 0126 0v10" fill="none" stroke="#fff" stroke-width="6"/><rect x="3" y="26" width="44" height="32" rx="3" fill="#fff"/><circle cx="25" cy="40" r="4" fill="#2c7cc4"/></svg><span>User Login</span></div>
          <div class="cta">Click here</div>
        </div>
        <div class="access-box">
          <div class="top"><svg width="60" height="50" viewBox="0 0 60 50"><circle cx="22" cy="14" r="10" fill="#fff"/><path d="M2 48c0-14 9-21 20-21s20 7 20 21z" fill="#fff"/><circle cx="42" cy="12" r="8" fill="#fff" opacity=".75"/><path d="M34 24c12-3 24 4 24 20H46" fill="#fff" opacity=".75"/></svg><span>Registration</span></div>
          <div class="cta">Click here</div>
        </div>
      </div>
    </section>

    <section class="panel news">
      <div class="tabs"><span class="active">BH News</span><span>Upcoming Classes &amp; Events</span></div>
      <div class="cards">
        <article class="card"><div class="photo p1" role="img" aria-label="Family walking together outdoors"></div><p>Lorem Ipsum is simply dummy text of the printing and typesetting industry. Lorem Ipsum has been the industry's standard dummy text ever since the 1500s, when an unknown printer took a galley of type and scrambled it to make a type specimen book.</p><a class="btn">Read More</a></article>
        <article class="card"><div class="photo p2" role="img" aria-label="Hand holding a stethoscope"></div><p>Lorem Ipsum is simply dummy text of the printing and typesetting industry. Lorem Ipsum has been the industry's standard dummy text ever since the 1500s, when an unknown printer took a galley of type and scrambled it to make a type specimen book.</p><a class="btn">Read More</a></article>
        <article class="card"><div class="photo p3" role="img" aria-label="Nurse caring for a patient"></div><p>Lorem Ipsum is simply dummy text of the printing and typesetting industry. Lorem Ipsum has been the industry's standard dummy text ever since the 1500s, when an unknown printer took a galley of type and scrambled it to make a type specimen book.</p><a class="btn">Read More</a></article>
      </div>
    </section>
  </div>
</main>

<footer class="footer">
  <div class="wrap cols">
    <div class="f-address">
      <h4>Address</h4>
      <div class="map" role="img" aria-label="Street map showing the hospital location"></div>
      <p>Lorem Ipsum is simply dummy text of the printing and typesetting industry.<br>Phone: (555) 210-4400<br>Email: brackfield-hospital@info.com</p>
    </div>
    <div class="f-links">
      <h4>Important Links</h4>
      <ul><li>Home</li><li>Our services</li><li>Facilities &amp; Directions</li><li>Patient &amp; Visitor information</li><li>Find a doctor</li><li>Health &amp; Wellness</li></ul>
    </div>
    <div class="f-about">
      <div class="row h"><span class="ico"><svg width="26" height="26" viewBox="0 0 26 26"><path d="M10 2h6v8h8v6h-8v8h-6v-8H2v-6h8z" fill="#fff"/></svg></span>About us</div>
      <div class="row"><span class="ico"><svg width="20" height="20" viewBox="0 0 24 24"><path fill="#f1e6da" d="M6.6 10.8a15 15 0 006.6 6.6l2.2-2.2c.3-.3.7-.4 1-.2 1.1.4 2.3.6 3.6.6.6 0 1 .4 1 1V20c0 .6-.4 1-1 1C10.6 21 3 13.4 3 4c0-.6.4-1 1-1h3.5c.6 0 1 .4 1 1 0 1.3.2 2.5.6 3.6.1.3 0 .7-.2 1z"/></svg></span>(555) 210-4400</div>
      <div class="row"><span class="ico"><svg width="22" height="16" viewBox="0 0 24 18"><rect x="1" y="1" width="22" height="16" fill="none" stroke="#f1e6da" stroke-width="2"/><path d="M1 1l11 9 11-9" fill="none" stroke="#f1e6da" stroke-width="2"/></svg></span>brackfield-hospital@info.com</div>
    </div>
  </div>
  <div class="footbar">
    <div class="wrap">
      <div class="links">
        <div>Site Map · Privacy · Web Guide</div>
        <div>Referring Physicians &nbsp; Medical Professionals &nbsp; Giving &nbsp; Volunteering &nbsp; Careers &nbsp; Online Bill Pay</div>
      </div>
      <div class="social"><i></i><i></i><i></i><i></i><i></i><i></i></div>
    </div>
  </div>
</footer>

</body>
</html>
```